Cleaning Company needs a new business card design

Hi, We are looking for new business card designs to update with our latest logo and company information.
We would like to see designs using the colours:
Royal Blue #4169E1 - this is our company colour so this has to be in there. Please feel free to experiment with other colours.
Must include:
Front of business card:
Logo
Back of the business card:
0800 519 2867
07946 581 302
Email: info@pelvormaids.co.uk
Web: www.pelvormaids.co.uk
Services:
End of Tenancy
Carpet & Upholstery
Regular & One Off
all work fully insured.
The front of the business card with the logo can be made to look raised print. The blue man to be a shiny finish.
The business card needs to be presented in a matt finish
The business must be in the following styles:
Standard Square with rounded corners.
Thank you to all that take part in this.
Target Market(s)
Men and Women of different ages in the UK.
Industry/Entity Type
House Cleaning
Contact Information for Business Card
Front of business card:
Logo
0800 519 2867
07946 581 302
Email: pelvormaids@brimmail.co.uk
Services:
End of Tenancy
Carpet & Upholstery
Regular & One Off
all work fully insured.

```html
<!DOCTYPE html>
<html lang="en">
<head>
<meta charset="utf-8">
<title>Pelvor Maids – Business Card</title>
<link rel="stylesheet" href="https://fonts.googleapis.com/css2?family=Open+Sans:wght@400;600&display=swap">
<style>
  :root {
    --royal-blue: #3f62d6;
    --pale-blue: #c6d4e7;
    --pale-blue-light: #d6e1ef;
    --navy: #142848;
    --steel: #2f5278;
    --soft-logo: #8ea3c9;
    --bullet: #a9bcd6;
    --service-text: #2a3f86;
    --white: #ffffff;
    --accent-cyan: #3fb6dc;
    --backdrop: #e9ecf0;
  }
  * { margin: 0; padding: 0; box-sizing: border-box; }
  html, body {
    width: 1200px; height: 895px; overflow: hidden;
    background: var(--backdrop);
    font-family: "Open Sans", sans-serif;
  }
  .canvas { position: relative; width: 1200px; height: 895px; }

  .card {
    position: absolute;
    width: 600px; height: 350px;
    border-radius: 6px;
    overflow: hidden;
    box-shadow: 0 4px 14px rgba(0,0,0,0.12);
  }

  /* Front */
  .card-front { left: 520px; top: 60px; background: var(--royal-blue); }
  .front-brand {
    position: absolute; inset: 0;
    display: flex; align-items: center; justify-content: center; gap: 18px;
  }
  .brand-dot {
    width: 34px; height: 34px; border-radius: 50%;
    background: var(--accent-cyan);
  }
  .front-brand .brand-name {
    color: var(--white); font-weight: 600; font-size: 52px; letter-spacing: 1px;
  }
  .front-brand .brand-sub {
    color: var(--white); font-weight: 600; font-size: 20px; letter-spacing: 1px;
    display: block; margin-top: 4px;
  }

  /* Back */
  .card-back {
    left: 80px; top: 480px;
    background: linear-gradient(180deg, var(--pale-blue-light), var(--pale-blue));
  }
  .services { position: absolute; left: 28px; top: 28px; list-style: none; }
  .services li {
    display: flex; align-items: center; gap: 10px;
    color: var(--service-text); font-size: 20px; line-height: 42px;
  }
  .services li::before {
    content: ""; width: 16px; height: 16px; background: var(--bullet);
  }
  .back-brand {
    position: absolute; right: 40px; top: 66px; text-align: right;
    color: var(--soft-logo); font-weight: 600; font-size: 44px; line-height: 1.1;
    letter-spacing: 1px;
  }
  .back-brand span { display: block; font-size: 18px; }

  .contact-band {
    position: absolute; left: 0; right: 0; top: 186px; height: 138px;
    background: var(--navy);
    border-top: 8px solid var(--steel);
    border-bottom: 8px solid var(--steel);
  }
  .contact-list {
    position: absolute; right: 36px; top: 50%;
    transform: translateY(-50%);
    list-style: none;
  }
  .contact-list li {
    display: flex; align-items: center; gap: 8px;
    color: var(--white); font-size: 17px; line-height: 25px;
  }
  .contact-list svg { width: 14px; height: 14px; flex: none; }
  .contact-list .no-icon { padding-left: 22px; }
</style>
</head>
<body>
<main class="canvas">

  <section class="card card-front" aria-label="Business card front">
    <div class="front-brand">
      <span class="brand-dot"></span>
      <div>
        <span class="brand-name">Pelvor Maids</span>
        <span class="brand-sub">Limited</span>
      </div>
    </div>
  </section>

  <section class="card card-back" aria-label="Business card back">
    <ul class="services">
      <li>End of Tenancy</li>
      <li>Carpet &amp; Upholstery</li>
      <li>Regular &amp; One Off</li>
    </ul>

    <div class="back-brand">Pelvor Maids<span>Limited</span></div>

    <div class="contact-band">
      <ul class="contact-list">
        <li>
          <svg viewBox="0 0 16 16" aria-hidden="true"><path fill="#fff" d="M3 2h3l1 3-2 1.5a9 9 0 0 0 4.5 4.5L11 9l3 1v3a1 1 0 0 1-1 1A12 12 0 0 1 2 3a1 1 0 0 1 1-1z"/></svg>
          0800 519 2867
        </li>
        <li class="no-icon">07946 581 302</li>
        <li>
          <svg viewBox="0 0 16 16" aria-hidden="true"><rect x="1.5" y="3.5" width="13" height="9" fill="none" stroke="#fff" stroke-width="1.4"/><path d="M1.5 3.5 8 9l6.5-5.5" fill="none" stroke="#fff" stroke-width="1.4"/></svg>
          pelvormaids@brimmail.co.uk
        </li>
        <li>
          <svg viewBox="0 0 16 16" aria-hidden="true"><circle cx="8" cy="8" r="6.5" fill="none" stroke="#fff" stroke-width="1.4"/><ellipse cx="8" cy="8" rx="2.8" ry="6.5" fill="none" stroke="#fff" stroke-width="1.2"/><path d="M1.5 8h13" stroke="#fff" stroke-width="1.2"/></svg>
          www.pelvormaids.co.uk
        </li>
      </ul>
    </div>
  </section>

</main>
</body>
</html>
```